Biz Card Design BTPW

New business card for a new company.
Logo was completed by a designer on ArtFlock and looking to continue requesting additional services.
Company Name: Bright Tidal Power Works
Although this company is starting in Canada, we will be moving towards a global presence within the next 6 months.
Key elements to this business are as follows.
Energy Procurement
Energy Reduction Services
Demand Side Consulting
Energy Efficiency Consulting
Saving Clients Money
Helping Them Go "Green"
Managing Their Energy Requirements
Basically the goal for our company is to find the best procurement solution for our clients and reduce their energy consumption. This reduces their expenses and the amount of greenhouse gas they produce on a daily basis.
I have been in the energy footprint for the last 20 years and know that most companies are looking to "do whatever is necessary to get them to sign on the dotted line". I would prefer to walk away from a client that I can't help than to put them into a situation that they will regret for years to come. This is where the "BRIGHT" part of the company name comes from.
The following is a catch phrase that encompasses what we do.
"Reducing your carbon footprint & energy bill at the same time!"
The back of the card needs to have this statement along with some sort of illustration. The back is a playground for creative ideas.
The front of the card needs the following.
Logo.
First & Last Name (Ned Varsolo)
Title (Energy Warrior)
Phone Number (555) 314-2769
Fax Number (555) 871-4420
Email Address ned@brighttidalpowerworks.example
Address 47 elmwick ave Toronto Ontario K2K 2K2
I want it to be a card that is remembered when any of my staff give it to a customer. It HAS to stand out.
Target Market(s)
Business Owners, Decision Makers, 30 to 65+
Industry/Entity Type
Business
Look and feel
Each slider illustrates characteristics of the customer's brand and the style your logo design should communicate.

```html
<!DOCTYPE html>
<html lang="en">
<head>
<meta charset="utf-8">
<title>Bright Tidal Power Works — Business Card</title>
<link rel="stylesheet" href="https://fonts.googleapis.com/css2?family=Lexend:wght@600&family=Questrial&display=swap">
<style>
  :root {
    --paper: #ffffff;
    --ink: #1a1a1a;
    --brand-blue: #3f74c0;
    --green-deep: #008a3e;
    --green-mid: #2ea356;
    --green-light: #9ccc7c;
    --ribbon-dark: #0f86c9;
    --ribbon-light: #8fbfe4;
    --ribbon-fold: #0a6aa6;
  }
  html, body {
    margin: 0;
    padding: 0;
    width: 1200px;
    height: 686px;
    overflow: hidden;
    background: var(--paper);
  }
  .card {
    position: relative;
    width: 1200px;
    height: 686px;
    background: var(--paper);
    overflow: hidden;
    font-family: "Questrial", "Helvetica Neue", Arial, sans-serif;
    color: var(--ink);
  }
  .brand-name {
    position: absolute;
    left: 50px;
    top: 160px;
    width: 580px;
    margin: 0;
    text-align: center;
    font-family: "Lexend", "Helvetica Neue", Arial, sans-serif;
    font-weight: 600;
    font-size: 40px;
    letter-spacing: -0.5px;
    color: var(--brand-blue);
  }
  .accent-panel {
    position: absolute;
    left: 679px;
    top: 0;
    width: 489px;
    height: 686px;
    background: linear-gradient(225deg, var(--green-light) 0%, var(--green-mid) 40%, var(--green-deep) 100%);
  }
  .name-ribbon {
    position: absolute;
    left: 639px;
    top: 282px;
    width: 561px;
    height: 116px;
    background: linear-gradient(90deg, var(--ribbon-dark) 0%, var(--ribbon-dark) 55%, var(--ribbon-light) 100%);
    color: var(--paper);
    text-align: center;
  }
  .ribbon-fold {
    position: absolute;
    left: 639px;
    top: 398px;
    width: 40px;
    height: 16px;
  }
  .person-name {
    margin: 20px 0 0 0;
    font-family: "Lexend", "Helvetica Neue", Arial, sans-serif;
    font-weight: 600;
    font-size: 43px;
    line-height: 1.05;
    padding-right: 40px;
  }
  .person-title {
    margin: 2px 0 0 0;
    font-size: 26px;
    letter-spacing: 0.5px;
    padding-right: 40px;
  }
  .contact {
    position: absolute;
    left: 20px;
    top: 510px;
    width: 600px;
    margin: 0;
    text-align: center;
    font-size: 25px;
    line-height: 34.5px;
    font-style: normal;
  }
  .contact .label {
    color: var(--brand-blue);
    font-family: "Lexend", "Helvetica Neue", Arial, sans-serif;
    font-weight: 600;
    font-size: 22px;
  }
</style>
</head>
<body>
  <div class="card">
    <h1 class="brand-name">Bright Tidal Power Works</h1>

    <div class="accent-panel" role="img" aria-label="Green gradient panel"></div>

    <svg class="ribbon-fold" viewBox="0 0 40 16" aria-hidden="true">
      <polygon points="0,0 40,0 40,16" fill="var(--ribbon-fold)"/>
    </svg>
    <div class="name-ribbon">
      <p class="person-name">Ned Varsolo</p>
      <p class="person-title">Energy Warrior</p>
    </div>

    <address class="contact">
      <div class="contact-address">47 elmwick ave Toronto Ontario K2K 2K2</div>
      <div><span class="label">Ph:</span> (555) 314-2769</div>
      <div><span class="label">Fax:</span> (555) 871-4420</div>
      <div><span class="label">Email:</span> ned@brighttidalpowerworks.example</div>
    </address>
  </div>
</body>
</html>
```